Meridale painting

We are a Painting company. We paint residential and commercial, interior& exterior painting, cabinets refinish,acoustic ceiling painting,popcorn ceiling removal,drywall repair,iron and concrete painting

We don't have any Facebook page or website.

We are a Painting company. We paint residential and commercial, interior& exterior painting, cabinets refinish,acoustic ceiling painting,popcorn ceiling removal,drywall repair,iron and concrete painting We don't have any Facebook page or website.

Requirements
Must have
• I need 200 cards. 50 of with my name Tobin, 50 with Owen 50 with Harold qnd 50 with bastian

```html
<!DOCTYPE html>
<html lang="en">
<head>
<meta charset="utf-8">
<title>Meridale Painting – Business Card</title>
<link rel="stylesheet" href="https://fonts.googleapis.com/css2?family=Montserrat:wght@400;600;700&display=swap">
<style>
  :root {
    --page-bg: #e9e9ec;
    --card-bg: #1c1c1e;
    --brand-blue: #1ea7e4;
    --accent-yellow: #ffe01a;
    --splash-blue: #1ea7e4;
    --splash-magenta: #c3168a;
    --splash-red: #e2231d;
    --splash-orange: #f26a1b;
    --splash-yellow: #ffe01a;
    --text-light: #f2f2f2;
  }
  html, body {
    margin: 0;
    width: 1200px;
    height: 900px;
    overflow: hidden;
    background: var(--page-bg);
    font-family: "Montserrat", sans-serif;
  }
  .business-card {
    position: absolute;
    left: 100px;
    top: 164px;
    width: 1000px;
    height: 572px;
    background: var(--card-bg);
    border-radius: 36px;
    overflow: hidden;
  }
  .paint-splash {
    position: absolute;
    left: -20px;
    top: 190px;
    width: 600px;
    height: 400px;
    border-radius: 48% 52% 0 0 / 60% 55% 0 0;
    background:
      radial-gradient(circle at 30% 85%, var(--splash-yellow) 0 22%, transparent 45%),
      linear-gradient(100deg, var(--splash-blue) 0%, var(--splash-magenta) 28%, var(--splash-red) 55%, var(--splash-orange) 75%, var(--splash-yellow) 100%);
  }
  .brand-name {
    position: absolute;
    right: 64px;
    top: 58px;
    margin: 0;
    text-align: right;
    color: var(--brand-blue);
    font-weight: 600;
    font-size: 62px;
    line-height: 1.05;
    letter-spacing: 3px;
    text-transform: uppercase;
  }
  .brand-name .line { display: block; }
  .contact-block {
    position: absolute;
    right: 64px;
    top: 262px;
    text-align: right;
    color: var(--text-light);
  }
  .holder-name {
    margin: 0 0 18px;
    color: var(--accent-yellow);
    font-weight: 700;
    font-size: 34px;
  }
  .address {
    margin: 0 0 14px;
    font-size: 19px;
    line-height: 1.35;
    padding-right: 44px;
  }
  .contact-line {
    display: flex;
    justify-content: flex-end;
    align-items: center;
    gap: 14px;
    margin: 0 0 10px;
    font-size: 19px;
  }
  .contact-icon {
    width: 30px;
    height: 30px;
    flex: none;
  }
</style>
</head>
<body>
  <main class="business-card">
    <div class="paint-splash" role="img" aria-label="Colourful paint splash in blue, magenta, red, orange and yellow"></div>

    <h1 class="brand-name"><span class="line">Meridale</span><span class="line">Painting</span></h1>

    <section class="contact-block">
      <p class="holder-name">bastian</p>
      <p class="address">Here is your Address<br>Road no. 123 USA</p>
      <p class="contact-line">
        <span>555.0148236</span>
        <svg class="contact-icon" viewBox="0 0 30 30" aria-hidden="true">
          <circle cx="15" cy="15" r="15" fill="#1ea7e4"/>
          <path d="M10 9c1-1 2-1 2.6 0l1.4 2.2c.4.7.2 1.4-.4 1.8l-.8.6c.8 1.8 2 3 3.8 3.8l.6-.8c.4-.6 1.1-.8 1.8-.4L21 17.6c1 .6 1 1.6 0 2.6-1.6 1.6-4.4 1-7.4-2S8.4 10.6 10 9z" fill="#fff"/>
        </svg>
      </p>
      <p class="contact-line">
        <span>info@meridalemail.com</span>
        <svg class="contact-icon" viewBox="0 0 30 30" aria-hidden="true">
          <circle cx="15" cy="15" r="15" fill="#ffe01a"/>
          <rect x="8" y="10" width="14" height="10" rx="1.5" fill="none" stroke="#1c1c1e" stroke-width="1.8"/>
          <path d="M8.5 10.8 15 16l6.5-5.2" fill="none" stroke="#1c1c1e" stroke-width="1.8"/>
        </svg>
      </p>
    </section>
  </main>
</body>
</html>
```